Business card for plumber

I need a business card for my plumbing company.
on it should:
Surname
position
E-mail
Telephone & mobile phone
Website
Please everything as placeholders / fantasy names.
We stand for high quality, hygiene and professionalism.

Colours:
# 606060 anthracite
# f7931e orange
# 2b89cc blue

Industry/Entity Type

Plumber

Contact Information for Business Card

folgt...

```html
<!DOCTYPE html>
<html lang="en">
<head>
<meta charset="utf-8">
<title>Bergwald Haustechnik – Business Card</title>
<link href="https://fonts.googleapis.com/css2?family=Roboto:wght@400;500;700&display=swap" rel="stylesheet">
<style>
  :root {
    --anthracite: #606060;
    --orange: #f7931e;
    --blue: #2b89cc;
    --text-grey: #555555;
    --backdrop: #9b9b9b;
    --white: #ffffff;
  }
  * { margin: 0; padding: 0; box-sizing: border-box; }
  html, body {
    width: 1021px; height: 1200px; overflow: hidden;
    background: var(--backdrop);
    font-family: "Roboto", sans-serif;
  }
  .canvas { position: relative; width: 1021px; height: 1200px; }
  .card {
    position: absolute; left: 139px; width: 744px; height: 425px; overflow: hidden;
  }
  .card--front { top: 121px; background: var(--anthracite); }
  .card--back { top: 653px; background: var(--white); }

  .brand { position: absolute; display: flex; align-items: center; gap: 14px; }
  .brand__mark { border-radius: 50%; flex: none; }
  .brand__name { font-weight: 700; line-height: 1; }
  .brand__name span { display: block; }
  .brand__name .brand__sub { letter-spacing: 0.36em; }

  .card--front .brand { left: 170px; top: 166px; }
  .card--front .brand__mark { width: 80px; height: 80px; background: var(--orange); }
  .card--front .brand__name { color: var(--orange); font-size: 44px; }
  .card--front .brand__sub { font-size: 22px; margin-top: 6px; }

  .card--back .brand { left: 58px; top: 165px; }
  .card--back .brand__mark { width: 70px; height: 70px; background: var(--blue); }
  .card--back .brand__name { color: var(--blue); font-size: 35px; }
  .card--back .brand__sub { font-size: 17px; margin-top: 5px; }

  .divider {
    position: absolute; left: 402px; top: 129px; width: 2px; height: 153px; background: var(--blue);
  }
  .contact { position: absolute; left: 416px; top: 127px; }
  .contact__name { color: var(--blue); font-weight: 700; font-size: 27px; letter-spacing: 0.01em; }
  .contact__role { color: var(--text-grey); font-size: 19px; margin-top: 4px; }
  .contact__list { list-style: none; margin-top: 14px; }
  .contact__item {
    display: flex; align-items: center; gap: 4px;
    color: var(--text-grey); font-size: 20px; height: 26px;
  }
  .contact__item svg { width: 17px; height: 17px; fill: var(--orange); flex: none; }

  .tagline {
    position: absolute; left: 0; top: 375px; width: 744px; height: 33px;
    background: var(--blue); color: var(--white); font-size: 19px;
    display: flex; align-items: center; justify-content: center;
  }
</style>
</head>
<body>
<main class="canvas">
  <section class="card card--front" aria-label="Card front">
    <div class="brand">
      <div class="brand__mark"></div>
      <div class="brand__name"><span>BERGWALD</span><span class="brand__sub">HAUSTECHNIK</span></div>
    </div>
  </section>

  <section class="card card--back" aria-label="Card back">
    <div class="brand">
      <div class="brand__mark"></div>
      <div class="brand__name"><span>BERGWALD</span><span class="brand__sub">HAUSTECHNIK</span></div>
    </div>
    <div class="divider"></div>
    <div class="contact">
      <p class="contact__name">JONAS KELLERT</p>
      <p class="contact__role">President</p>
      <ul class="contact__list">
        <li class="contact__item">
          <svg viewBox="0 0 24 24" aria-hidden="true"><path d="M6.6 10.8a15 15 0 0 0 6.6 6.6l2.2-2.2c.3-.3.7-.4 1-.2 1.1.4 2.3.6 3.6.6.6 0 1 .4 1 1V20c0 .6-.4 1-1 1C10.6 21 3 13.4 3 4c0-.6.4-1 1-1h3.5c.6 0 1 .4 1 1 0 1.3.2 2.5.6 3.6.1.3 0 .7-.2 1z"/></svg>
          555 014 2087
        </li>
        <li class="contact__item">
          <svg viewBox="0 0 24 24" aria-hidden="true"><path d="M7 1h10a2 2 0 0 1 2 2v18a2 2 0 0 1-2 2H7a2 2 0 0 1-2-2V3a2 2 0 0 1 2-2zm0 3v14h10V4zm5 15.5a1 1 0 1 0 0 2 1 1 0 0 0 0-2z"/></svg>
          555 014 2088
        </li>
        <li class="contact__item">
          <svg viewBox="0 0 24 24" aria-hidden="true"><path d="M3 6h18v2l-9 5-9-5zm0 4 9 5 9-5v8H3z"/></svg>
          info@bergwaldhaustec.com
        </li>
        <li class="contact__item">
          <svg viewBox="0 0 24 24" aria-hidden="true"><path d="M12 2a10 10 0 1 0 0 20 10 10 0 0 0 0-20zm-1 17.9A8 8 0 0 1 4.1 10L9 15v1a2 2 0 0 0 2 2zm6.9-2.5A2 2 0 0 0 16 16h-1v-3a1 1 0 0 0-1-1H8v-2h2a1 1 0 0 0 1-1V7h2a2 2 0 0 0 2-2v-.4a8 8 0 0 1 2.9 12.8z"/></svg>
          www.bergwaldhaustec.com
        </li>
      </ul>
    </div>
    <p class="tagline">We stand for high quality, hygiene and professionalism.</p>
  </section>
</main>
</body>
</html>
```